Wine Labels for new product to attract Millenial consumers

SipRoam Design Brief
1. Intro:
Marrabel Cellars is a 120 year old family owned Australian wine company renowned for producing traditional premium quality wines. This project is aimed at breaking through this perception of Marrabel to show main stream Australian retailers that we can be innovative and relevant and that we know who their millennial shoppers are and we know how to attract their attention. This needs to be achieved through the combination of innovative and clever design paired with a product that challenges conventional Australian wine philosophies and appeals to those wine drinkers seeking authentic and alternative wine experiences.
2. Feelings:
This new wine should evoke a new set of feelings in retailers that they don’t usually associate with Marrabel Cellars. Retailers should feel excited, challenged and impressed by our knowledge of the millennial demographic. The packaging should make the shopper feel surprised, curious, cool, aspirational, understood, adventurous, individual, fashionable, progressive and engaged. It also needs to evoke a sense of the occasion it should be consumed in, with food and friends in a fun environment and evoke a sense of conviviality and a desire for shared social interaction.
3. Look + Feel:
It shouldn’t look or feel like anything Marrabel Cellars is known for and has done before. It should not carry our branding or logo, this should be a standalone product range. It should feel modern, cool, clever and hip. It should feel real, authentic, artisanal and most of all it should challenge the traditional visual discourse of wine as bored, tired, stiff and conservative. The design should be respected piece of art in its own right. It should make the shopper feel like getting a few friends around for dinner and drinks.
4. Brand Position:
This product range needs to challenge the existing brand positioning of Marrabel Cellars. It should clearly target the millennial demographic and the hipster sub culture who are being lured into new alcohol categories by cool design and positioning. “Exposed to a barrage of drinks offerings, the report found that wine is in danger of losing Generation Y to other more engaging drinks categories such as beer, cider and spirits ……. With 18-25 year olds accounting for 25% of the wine drinking population, Millennials represent an important sector of the wine market, thus keeping their attention and interest should remain a priority for wine brands.” Grape Insight Review. “…. Wine is becoming increasingly cool with the influencers and trend setters of a whole new generation.” Pour Journal.
5. Needs:
2 wine labels, one white and one red, but linked by design. Should fit a 500 ml glass bottle and design should be able to carry over to some innovative packaging into small lots of 4 or 6 like beer. For the purpose of design use the name SipRoam White and SipRoam Red. Relating the wine to food and how it should be consumed is important as this needs to be seen as a lifestyle accessory to food to combat the anti-alcohol lobby and the socially acceptable practise of eating and drinking together as part of a social experience. An area for approximately 200 words of mandatory information and declarations needs to be provided.

https://www.examplepins.test/MarrabelCellars/siproam-moodboard/

Full brief in project description

Requirements
Must have
• Full brief in project description
Nice to have
Should not have

```html
<!DOCTYPE html>
<html lang="en">
<head>
<meta charset="utf-8">
<title>SipRoam Red and SipRoam White labels</title>
<link rel="stylesheet" href="https://fonts.googleapis.com/css2?family=Monoton&family=Kaushan+Script&family=Josefin+Sans:wght@300;400&display=swap">
<style>
  :root {
    --wine-red: #9b0d12;
    --wine-red-deep: #7a0a0e;
    --paper: #ffffff;
    --ink-grey: #6d6d6d;
    --stage-dark: #c9c9c9;
    --stage-light: #ffffff;
    --red-label-a: #b9d3e6;
    --red-label-b: #e6c3cf;
    --red-label-c: #f3e6e6;
    --white-label-a: #7fb7c7;
    --white-label-b: #c58fae;
    --white-label-c: #4a4fa6;
    --wheel-red: #c0282d;
    --wheel-white: #f4f4f4;
  }
  * { box-sizing: border-box; margin: 0; padding: 0; }
  html, body { width: 1200px; height: 881px; overflow: hidden; }
  body {
    position: relative;
    background: linear-gradient(90deg, var(--stage-dark) 0%, #e7e7e7 40%, var(--stage-light) 70%, #f3f3f3 100%);
    font-family: "Josefin Sans", sans-serif;
  }
  .wordmark {
    position: absolute;
    font-family: "Monoton", sans-serif;
    white-space: nowrap;
    line-height: 1;
  }
  .wordmark--side-left {
    left: 62px; top: 800px;
    font-size: 100px;
    color: var(--paper);
    -webkit-text-stroke: 1px #8a8a8a;
    transform: rotate(-90deg);
    transform-origin: 0 0;
  }
  .wordmark--side-right {
    left: 1162px; top: 62px;
    font-size: 100px;
    color: var(--wine-red);
    transform: rotate(90deg);
    transform-origin: 0 0;
  }
  .wordmark--float-top {
    left: 420px; top: 140px;
    font-size: 50px;
    color: var(--paper);
    -webkit-text-stroke: 1px #9a9a9a;
    transform: rotate(9deg);
  }
  .wordmark--float-bottom {
    left: 440px; top: 745px;
    font-size: 52px;
    color: var(--wine-red);
    transform: rotate(-8deg);
  }
  .variety {
    position: absolute;
    font-family: "Kaushan Script", cursive;
    line-height: 1;
  }
  .variety--red {
    left: 515px; top: 330px;
    font-size: 92px;
    color: var(--wine-red);
    transform: rotate(-4deg);
  }
  .variety--white {
    left: 450px; top: 525px;
    font-size: 92px;
    color: var(--paper);
    -webkit-text-stroke: 1px #b5b5b5;
    transform: rotate(-10deg);
  }
  .cycle {
    position: absolute;
    border-radius: 50%;
  }
  .cycle--penny {
    left: 650px; top: 390px; width: 145px; height: 145px;
    background: radial-gradient(circle, rgba(192,40,45,0.15) 0%, rgba(192,40,45,0.45) 60%, rgba(192,40,45,0) 72%);
  }
  .cycle--road {
    left: 585px; top: 615px; width: 150px; height: 110px;
    border-radius: 40%;
    background: radial-gradient(ellipse, rgba(255,255,255,0.9) 0%, rgba(255,255,255,0.6) 55%, rgba(255,255,255,0) 72%);
  }
  .label {
    position: absolute;
    width: 184px; height: 350px;
    display: flex; flex-direction: column; align-items: center;
    padding-top: 34px;
    box-shadow: 0 6px 18px rgba(0,0,0,0.18);
  }
  .label--red {
    left: 240px; top: 325px;
    background: linear-gradient(160deg, var(--red-label-a) 0%, var(--red-label-b) 50%, var(--red-label-c) 100%);
  }
  .label--white {
    left: 800px; top: 340px;
    background: linear-gradient(165deg, var(--white-label-a) 0%, #b7a7b8 45%, var(--white-label-b) 70%, var(--white-label-c) 100%);
  }
  .label__volume {
    font-size: 14px; letter-spacing: 2px; font-weight: 300;
  }
  .label--red .label__volume { color: var(--wine-red-deep); }
  .label--white .label__volume { color: var(--paper); }
  .label__cycle {
    margin-top: 14px; width: 110px; height: 78px; border-radius: 40%;
  }
  .label--red .label__cycle { background: radial-gradient(ellipse, rgba(192,40,45,0.35), rgba(192,40,45,0) 70%); }
  .label--white .label__cycle { background: radial-gradient(ellipse, rgba(255,255,255,0.8), rgba(255,255,255,0) 70%); }
  .label__swoosh { display: block; width: 160px; height: 22px; }
  .label__name {
    font-family: "Monoton", sans-serif;
    font-size: 25px; line-height: 1.1; margin-top: 2px;
  }
  .label--red .label__name { color: var(--wine-red); }
  .label--white .label__name { color: var(--paper); -webkit-text-stroke: 0.6px #8a8a8a; }
  .label__variety {
    font-family: "Kaushan Script", cursive;
    font-size: 40px; line-height: 1; margin: 2px 0 4px;
  }
  .label--red .label__variety { color: var(--wine-red); }
  .label--white .label__variety { color: var(--paper); }
</style>
</head>
<body>
  <div class="wordmark wordmark--side-left">SipRoam</div>
  <div class="wordmark wordmark--side-right">SipRoam</div>
  <div class="wordmark wordmark--float-top">SipRoam</div>

  <div class="variety variety--red">Red</div>
  <div class="cycle cycle--penny" role="img" aria-label="Red line illustration of a penny-farthing bicycle"></div>
  <div class="variety variety--white">White</div>
  <div class="cycle cycle--road" role="img" aria-label="White line illustration of a road bicycle"></div>

  <div class="wordmark wordmark--float-bottom">SipRoam</div>

  <section class="label label--red" aria-label="SipRoam Red label">
    <p class="label__volume">500 ML</p>
    <div class="label__cycle" role="img" aria-label="Penny-farthing bicycle illustration"></div>
    <svg class="label__swoosh" viewBox="0 0 160 22"><path d="M4 18 Q80 0 156 8" fill="none" stroke="var(--wine-red)" stroke-width="3" stroke-linecap="round"/></svg>
    <p class="label__name">SipRoam</p>
    <p class="label__variety">Red</p>
    <svg class="label__swoosh" viewBox="0 0 160 22"><path d="M4 6 Q80 24 156 10" fill="none" stroke="var(--wine-red)" stroke-width="3" stroke-linecap="round"/></svg>
  </section>

  <section class="label label--white" aria-label="SipRoam White label">
    <p class="label__volume">500 ML</p>
    <div class="label__cycle" role="img" aria-label="Road bicycle illustration"></div>
    <svg class="label__swoosh" viewBox="0 0 160 22"><path d="M4 18 Q80 0 156 8" fill="none" stroke="var(--paper)" stroke-width="3" stroke-linecap="round"/></svg>
    <p class="label__name">SipRoam</p>
    <p class="label__variety">White</p>
    <svg class="label__swoosh" viewBox="0 0 160 22"><path d="M4 6 Q80 24 156 10" fill="none" stroke="var(--paper)" stroke-width="3" stroke-linecap="round"/></svg>
  </section>
</body>
</html>
```